Business card for Les Brisants-Corail campsite

HORIZONTAL / 85x55
OBJECTIVE
Create a modern, attractive and memorable business card for the Les Brisants-Corail campsite, located on the Île d'Oléron.
The map should make people want to discover the campsite and immediately convey its world: ocean, holidays, nature and conviviality.
VISUAL IDENTITY
The design must be in the same graphic style as our website:
www.lesbrisants-corail.fr
The site is the main reference for the visual atmosphere: colours, typography, shapes, photographs and general universe.
The map and the site must give the impression of belonging to a single brand identity.
A UNIVERSE TO TRANSMIT
• Île d'Oléron
• Atlantic Ocean
• Seaside
• Direct access to the beaches
• Vacation
• Nature
• Family-friendly and welcoming atmosphere
• Relaxation
DESIRED STYLE
Bright, warm, modern, nautical and natural.
We want a creation with a real personality, immediately recognizable, and not a generic camping business card.
FRONT
Prioritize visual impact with:
• Official logo Les Brisants-Corail
• Île d'Oléron
• A strong evocation of the ocean and holidays
• A short and memorable hook
The designer is free to propose their own hook.
BACK
The Coral Breakers
Villages 1 & 2
22 Rue des Mouettes
17310 Saint-Pierre-d'Oléron
France
Tel.: +33 5 47 12 38 04
www.lesbrisants-corail. fr
Possibility of discreet integration:
Direct access to the beaches
Mobile homes • Pitches • Accommodation
Le Varech Bar-Restaurant
FORMAT
Double-sided card: 85 × 55 mm.
Horizontal orientation
AVOID
• Overly institutional design
• Overloaded map
• Generic "camping" style
• Too many pictograms
• Accumulation of texts
• Modification or distortion of the official logo
• Graphic design unrelated to the website
CREATIVE FREEDOM
We are looking for an original proposal.
The designer can play with the graphic codes of the ocean, waves, sun, beach and Île d'Oléron, while remaining faithful to the visual identity of the site.
The card must be aesthetically pleasing and original enough to make people want to keep it.
The objective:
See the map → think about the ocean and holidays → remember Les Brisants-Corail → discover the campsite.
Target Market(s)
All targets
Industry/Entity Type
Tourisme
Contact Information for Business Card
adresse, téléphone, email, site internet + réseaux sociaux
Look and feel
Each slider illustrates characteristics of the customer's brand and the style your logo design should communicate.

```html
<!DOCTYPE html>
<html lang="fr">
<head>
<meta charset="utf-8">
<title>Les Brisants-Corail – Carte de visite</title>
<link rel="stylesheet" href="https://fonts.googleapis.com/css2?family=Poppins:wght@400;500;600&display=swap">
<style>
  :root {
    --stage: #474747;
    --card: #ffffff;
    --ink: #3d4147;
    --deep-teal: #0f4a5a;
    --black: #141414;
    --blue: #29a8e0;
    --lime: #a9cc3a;
    --lime-pale: #e6f0c4;
    --frame: #4a4d52;
  }
  * { box-sizing: border-box; margin: 0; padding: 0; }
  html, body { width: 1200px; height: 1200px; overflow: hidden; }
  body {
    background: var(--stage);
    font-family: "Poppins", sans-serif;
    position: relative;
  }
  .card {
    position: absolute;
    left: 229px;
    width: 743px;
    height: 481px;
    overflow: hidden;
  }
  .card--front { top: 92px; }
  .card--back { top: 627px; background: var(--card); }

  /* Front */
  .beach-scene {
    position: absolute; inset: 0;
    background: linear-gradient(180deg, #b3dfe8 0%, #f3ebc8 32%, #9fd0d8 48%, #6bbfcc 68%, #e6d4a2 86%, #e3c07e 100%);
  }
  .brand-name {
    position: absolute;
    top: 170px; left: 0; right: 0;
    text-align: center;
    font-weight: 600;
    font-size: 46px;
    color: var(--ink);
  }
  .brand-name::before {
    content: "";
    display: inline-block;
    width: 30px; height: 30px;
    border-radius: 50%;
    background: var(--blue);
    margin-right: 14px;
    vertical-align: -2px;
  }
  .hook {
    position: absolute;
    top: 322px; left: 0; right: 0;
    text-align: center;
    font-weight: 600;
    font-size: 48px;
    color: var(--deep-teal);
    letter-spacing: -.5px;
  }
  .subhook {
    position: absolute;
    top: 400px; left: 0; right: 0;
    text-align: center;
    font-size: 32px;
    color: var(--black);
  }

  /* Back */
  .brand-strip {
    position: absolute;
    left: 29px; top: 43px;
    width: 686px; height: 131px;
    border: 2px solid var(--frame);
    border-radius: 10px;
    display: flex;
    align-items: center;
    justify-content: space-around;
    padding: 0 10px;
  }
  .brand-mark {
    font-weight: 600;
    font-size: 21px;
    color: var(--ink);
    text-align: center;
    line-height: 1.25;
  }
  .brand-mark small {
    display: block;
    font-weight: 500;
    font-size: 11px;
    letter-spacing: 2.5px;
    text-transform: uppercase;
    margin-top: 6px;
  }
  .contact-title {
    position: absolute;
    left: 29px; top: 223px;
    width: 204px; height: 27px;
    border-radius: 14px;
    background: var(--blue);
    color: #fff;
    font-weight: 600;
    font-size: 18px;
    line-height: 27px;
    padding-left: 22px;
  }
  .contact-list { position: absolute; left: 33px; top: 271px; list-style: none; }
  .contact-item {
    display: flex; align-items: flex-start;
    font-size: 18.5px; color: var(--ink);
    line-height: 22px;
    margin-bottom: 17px;
  }
  .contact-item svg { width: 24px; height: 24px; margin-right: 16px; flex: none; }
  .divider {
    position: absolute; left: 378px; top: 207px;
    width: 1.5px; height: 204px; background: #555;
  }
  .feature {
    position: absolute;
    width: 160px;
    text-align: center;
    font-size: 18px;
    line-height: 20px;
    color: var(--ink);
  }
  .feature-icon {
    display: block;
    margin: 0 auto 14px;
    width: 50px; height: 48px;
    border-radius: 10px;
    background: var(--lime-pale);
  }
  .ground-curve { position: absolute; left: 150px; top: 448px; width: 460px; height: 33px; }
</style>
</head>
<body>

<section class="card card--front">
  <div class="beach-scene" role="img" aria-label="Plage ensoleillée au bord de l'océan Atlantique, ciel clair et soleil"></div>
  <p class="brand-name">Les Brisants-Corail</p>
  <p class="hook">L’océan à vos pieds.</p>
  <p class="subhook">Vos vacances ensoleillées.</p>
</section>

<section class="card card--back">
  <div class="brand-strip">
    <p class="brand-mark">Les Brisants-Corail<small>Village 1</small></p>
    <p class="brand-mark">Les Brisants-Corail<small>Village 2</small></p>
    <p class="brand-mark">Le Varech<small>Bar / Restaurant</small></p>
  </div>

  <p class="contact-title">Coordonnées</p>
  <ul class="contact-list">
    <li class="contact-item">
      <svg viewBox="0 0 24 24" fill="none" stroke="#29a8e0" stroke-width="1.6"><circle cx="12" cy="12" r="10.5"/><path d="M8.5 6.5l2 2.5-1.2 1.4c.8 1.7 2 2.9 3.6 3.7l1.4-1.2 2.5 2-1.2 1.8c-4.2-.4-8-4.2-8.6-8.5z"/></svg>
      +33 5 47 12 38 04
    </li>
    <li class="contact-item">
      <svg viewBox="0 0 24 24" fill="none" stroke="#29a8e0" stroke-width="1.6"><circle cx="12" cy="12" r="10.5"/><ellipse cx="12" cy="12" rx="4.5" ry="10.5"/><path d="M1.5 12h21M3.5 6.5h17M3.5 17.5h17"/></svg>
      www.lesbrisants-corail. fr
    </li>
    <li class="contact-item">
      <svg viewBox="0 0 24 24"><path d="M12 1.5a7 7 0 0 0-7 7c0 5 7 14 7 14s7-9 7-14a7 7 0 0 0-7-7z" fill="#29a8e0"/><circle cx="12" cy="8.5" r="2.6" fill="#fff"/></svg>
      <span>22 Rue des Mouettes 17310<br>Saint-Pierre-d'Oléron France</span>
    </li>
  </ul>

  <div class="divider"></div>

  <div class="feature" style="left:400px; top:206px;">
    <span class="feature-icon" role="img" aria-label="Pictogramme chemin vers la plage"></span>Accès direct<br>aux plages
  </div>
  <div class="feature" style="left:560px; top:206px;">
    <span class="feature-icon" role="img" aria-label="Pictogramme verre et couverts"></span>Bar-Restaurant<br>Le Varech
  </div>
  <div class="feature" style="left:400px; top:339px;">
    <span class="feature-icon" role="img" aria-label="Pictogramme tente et arbre"></span>Hébergements
  </div>
  <div class="feature" style="left:560px; top:339px;">
    <span class="feature-icon" role="img" aria-label="Pictogramme mobil-home"></span>Mobil-homes
  </div>

  <svg class="ground-curve" viewBox="0 0 460 33" preserveAspectRatio="none">
    <defs>
      <linearGradient id="groundTone" x1="0" x2="1">
        <stop offset="0" stop-color="#d9e236"/>
        <stop offset="1" stop-color="#a3cb3c"/>
      </linearGradient>
    </defs>
    <path d="M0 33 Q230 -20 460 33 Z" fill="url(#groundTone)"/>
  </svg>
</section>

</body>
</html>
```